mechanical repair shop

our shop repairs light and medium duty trucks

we sell tires , do oil changes, engine and transmissions
vehicle accessories, alignments, brakes , exhaust, all major and minor repairs.

if you would like to get a hold of me email: kelvin.moraday@quillstenworks.com tel: 1-555-418-3067

Target Market(s)

light and medium duty trucks and cars

Industry/Entity Type

Shop

Colors
f37122

Requirements
Must have
• visual sales displays
Nice to have
• pictures

```html
<!DOCTYPE html>
<html lang="en">
<head>
<meta charset="utf-8">
<title>Quillsten Works – Truck Repair Facility</title>
<link href="https://fonts.googleapis.com/css2?family=Oswald:wght@400;500;600&family=Montserrat:ital,wght@0,400;0,500;1,400&display=swap" rel="stylesheet">
<style>
:root{
  --orange:#f37122;
  --black:#050505;
  --white:#ffffff;
  --ink:#1b1b1b;
  --body:#333333;
  --stage:#3d3d3d;
}
*{margin:0;padding:0;box-sizing:border-box}
html,body{width:960px;height:1200px;overflow:hidden;background:var(--stage)}
.flyer{position:absolute;left:56px;top:0;width:848px;height:1200px;background:var(--white);overflow:hidden;font-family:"Montserrat",sans-serif}
.flyer-shapes{position:absolute;inset:0}
.truck-photo{position:absolute;left:215px;top:45px;width:632px;height:230px;background:linear-gradient(180deg,#f4f4f4 0%,#d9d9d9 55%,#3a3a3a 100%);clip-path:polygon(6% 0,100% 0,100% 100%,0 100%,0 40%)}
.brand{position:absolute;left:40px;top:360px;display:flex;align-items:center;gap:10px}
.brand-dot{width:22px;height:22px;border-radius:50%;background:var(--orange)}
.brand-name{font-family:"Oswald",sans-serif;font-weight:600;font-size:34px;letter-spacing:1px;color:var(--orange)}
.headline{position:absolute;left:524px;top:414px;font-family:"Oswald",sans-serif;font-weight:600;font-size:35px;line-height:44px;color:var(--ink);letter-spacing:-.5px;text-transform:uppercase}
.section-title{font-family:"Oswald",sans-serif;font-weight:500;font-size:40px;color:var(--ink);letter-spacing:-.5px;line-height:1}
.services{position:absolute;left:32px;top:540px}
.service-list{list-style:none;margin-top:18px}
.service-list li{display:flex;align-items:center;gap:10px;height:32.8px;font-size:15px;color:var(--body);letter-spacing:.2px}
.service-list svg{width:16px;height:16px;flex:none}
.shop-photo{position:absolute;top:615px;height:128px}
.shop-photo.tire{left:436px;width:192px;background:linear-gradient(135deg,#9a9a9a,#2a2a2a 60%,#6f6f6f)}
.shop-photo.oil{left:636px;width:192px;background:linear-gradient(135deg,#c9c9c9,#6a6a6a 50%,#c08a1e 75%,#8a8a8a)}
.about{position:absolute;left:432px;top:758px;width:395px}
.about p{margin-top:18px;font-style:italic;font-size:13.3px;line-height:21.4px;color:var(--ink)}
.website{position:absolute;left:37px;top:1146px;font-family:"Oswald",sans-serif;font-size:24px;color:var(--white)}
.contact{position:absolute;right:43px;top:1088px;text-align:right;font-family:"Oswald",sans-serif}
.contact-lead{font-size:24px;color:var(--orange);font-weight:400}
.contact-phone{display:flex;align-items:center;justify-content:flex-end;gap:10px;font-size:47px;color:var(--white);line-height:1.15;font-weight:400}
.contact-phone svg{width:28px;height:44px}
</style>
</head>
<body>
<main class="flyer">
  <svg class="flyer-shapes" viewBox="0 0 848 1200" width="848" height="1200" aria-hidden="true">
    <polygon points="0,0 290,66 847,66 847,327 0,510" fill="var(--black)"/>
    <polygon points="350,447 847,340 847,599 524,567" fill="var(--orange)"/>
    <polygon points="0,1089 282,1127 330,1200 0,1200" fill="var(--orange)"/>
    <polygon points="290,1120 728,1037 848,1084 848,1200 345,1200" fill="var(--black)"/>
  </svg>

  <div class="truck-photo" role="img" aria-label="Three white light and medium duty box trucks lined up"></div>

  <div class="brand"><span class="brand-dot"></span><span class="brand-name">QUILLSTEN</span></div>

  <h1 class="headline">Your Complete<br>Light &amp; Medium Duty<br>Truck Repair Facility</h1>

  <section class="services">
    <h2 class="section-title">Services We Offer:</h2>
    <ul class="service-list">
      <li><svg viewBox="0 0 16 16"><circle cx="8" cy="8" r="6.5" fill="none" stroke="#f37122" stroke-width="1.5"/><path d="M5 8.2l2.2 2.2L12.5 5" fill="none" stroke="#f37122" stroke-width="1.6"/></svg>Factory recommended service</li>
      <li><svg viewBox="0 0 16 16"><circle cx="8" cy="8" r="6.5" fill="none" stroke="#f37122" stroke-width="1.5"/><path d="M5 8.2l2.2 2.2L12.5 5" fill="none" stroke="#f37122" stroke-width="1.6"/></svg>Oil change</li>
      <li><svg viewBox="0 0 16 16"><circle cx="8" cy="8" r="6.5" fill="none" stroke="#f37122" stroke-width="1.5"/><path d="M5 8.2l2.2 2.2L12.5 5" fill="none" stroke="#f37122" stroke-width="1.6"/></svg>Fuel system repair and maintenance</li>
      <li><svg viewBox="0 0 16 16"><circle cx="8" cy="8" r="6.5" fill="none" stroke="#f37122" stroke-width="1.5"/><path d="M5 8.2l2.2 2.2L12.5 5" fill="none" stroke="#f37122" stroke-width="1.6"/></svg>Battery system diagnosis &amp; repair</li>
      <li><svg viewBox="0 0 16 16"><circle cx="8" cy="8" r="6.5" fill="none" stroke="#f37122" stroke-width="1.5"/><path d="M5 8.2l2.2 2.2L12.5 5" fill="none" stroke="#f37122" stroke-width="1.6"/></svg>Check engine light</li>
      <li><svg viewBox="0 0 16 16"><circle cx="8" cy="8" r="6.5" fill="none" stroke="#f37122" stroke-width="1.5"/><path d="M5 8.2l2.2 2.2L12.5 5" fill="none" stroke="#f37122" stroke-width="1.6"/></svg>Electrical problems</li>
      <li><svg viewBox="0 0 16 16"><circle cx="8" cy="8" r="6.5" fill="none" stroke="#f37122" stroke-width="1.5"/><path d="M5 8.2l2.2 2.2L12.5 5" fill="none" stroke="#f37122" stroke-width="1.6"/></svg>Engine performance</li>
      <li><svg viewBox="0 0 16 16"><circle cx="8" cy="8" r="6.5" fill="none" stroke="#f37122" stroke-width="1.5"/><path d="M5 8.2l2.2 2.2L12.5 5" fill="none" stroke="#f37122" stroke-width="1.6"/></svg>Exhaust problems</li>
      <li><svg viewBox="0 0 16 16"><circle cx="8" cy="8" r="6.5" fill="none" stroke="#f37122" stroke-width="1.5"/><path d="M5 8.2l2.2 2.2L12.5 5" fill="none" stroke="#f37122" stroke-width="1.6"/></svg>Tires</li>
      <li><svg viewBox="0 0 16 16"><circle cx="8" cy="8" r="6.5" fill="none" stroke="#f37122" stroke-width="1.5"/><path d="M5 8.2l2.2 2.2L12.5 5" fill="none" stroke="#f37122" stroke-width="1.6"/></svg>30/60/90 K mileage maintenance services</li>
      <li><svg viewBox="0 0 16 16"><circle cx="8" cy="8" r="6.5" fill="none" stroke="#f37122" stroke-width="1.5"/><path d="M5 8.2l2.2 2.2L12.5 5" fill="none" stroke="#f37122" stroke-width="1.6"/></svg>Cooling system repair and maintenance</li>
      <li><svg viewBox="0 0 16 16"><circle cx="8" cy="8" r="6.5" fill="none" stroke="#f37122" stroke-width="1.5"/><path d="M5 8.2l2.2 2.2L12.5 5" fill="none" stroke="#f37122" stroke-width="1.6"/></svg>Air conditioning / heating repair</li>
      <li><svg viewBox="0 0 16 16"><circle cx="8" cy="8" r="6.5" fill="none" stroke="#f37122" stroke-width="1.5"/><path d="M5 8.2l2.2 2.2L12.5 5" fill="none" stroke="#f37122" stroke-width="1.6"/></svg>Brake system</li>
      <li><svg viewBox="0 0 16 16"><circle cx="8" cy="8" r="6.5" fill="none" stroke="#f37122" stroke-width="1.5"/><path d="M5 8.2l2.2 2.2L12.5 5" fill="none" stroke="#f37122" stroke-width="1.6"/></svg>Steering &amp; suspension</li>
    </ul>
  </section>

  <div class="shop-photo tire" role="img" aria-label="Mechanic mounting a tire on a tire changer"></div>
  <div class="shop-photo oil" role="img" aria-label="Fresh motor oil being poured into an engine"></div>

  <section class="about">
    <h2 class="section-title">About Us:</h2>
    <p>Quillsten Works Ltd. has set up and successfully operates a complete equipment repair facility. First set up to be a dedicated repair shop for a single large client, Quillsten has now expanded to include all manner of clients with diverse equipment needs. With Journeyman and Apprentice HD mechanics available 24 hours a day our facility is ready to handle all of your equipment needs. We are an ‘approved’ repair facility for a growing list of equipment manufacturers including: Terravolt, Harlowe, Pinecrest, Kestrel, Ridgemark etc.</p>
  </section>

  <div class="website">www.quillstenworks.com</div>

  <div class="contact">
    <div class="contact-lead">Call us for more information</div>
    <div class="contact-phone">
      <svg viewBox="0 0 28 44" aria-hidden="true"><path d="M9 2c2 0 3 1 4 3l2 6c.5 2-1 3-3 4-1 .5-1 2-.5 4l3 7c1 2 2 2.5 3.5 2 2-.7 3.5-.7 4.5 1l3 5c1 2 0 3-2 4.5-3 2-7 1.5-10-4L4 22C1 14 2 7 5 4c1.5-1.5 2.5-2 4-2z" fill="#fff"/></svg>
      <span>555 418 3067</span>
    </div>
  </div>
</main>
</body>
</html>
```